Business supporting small business needs: Business card, A4 letterhead, A6 postcard, C5& C6envelope

We require stationery designed for a new Australian company called "Tallow Meadow" that provides operational strategy and support to small businesses.

We already have a logo (attached).

We require:
- business card (double-sided)
- A4 letterhead (double-sided)
- A6 postcard - to be used like a with-compliments slip (double-sided)
- C5 envelope
- C6 envelope

We would like the backs of the business card, letterhead and postcard to strongly feature the blue colour from the logo.

The business card, letterhead and postcard must contain:
- Tallow Meadow
- Staff member name
- Website address
- Email address
- Phone number
- Postal address
(I will provide these details to the winner)

The letterhead must also contain the ABN: 57 382 916 204 and company name "Tallow Meadow Pty Ltd".

Our standard font is century gothic.
Updates

Thank you for the designs so far.

Please note that the only change to the logo I am open to, is using an all white logo on a blue background.

I am not open to any other changes to the logo, such as shading, shadows or other colour changes.

Target Market(s)

Small and micro business owners

Industry/Entity Type

Small Business

```html
<!DOCTYPE html>
<html lang="en">
<head>
<meta charset="utf-8">
<title>Tallow Meadow – Stationery</title>
<link rel="stylesheet" href="https://fonts.googleapis.com/css2?family=Questrial&display=swap">
<style>
  :root {
    --brand-blue: #3aadd1;
    --brand-blue-deep: #35a2c4;
    --paper: #ffffff;
    --backdrop: #eef0f0;
    --text-blue: #3aadd1;
  }
  * { margin: 0; padding: 0; box-sizing: border-box; }
  html, body {
    width: 1200px;
    height: 900px;
    overflow: hidden;
    background: var(--backdrop);
    font-family: "Questrial", "Century Gothic", sans-serif;
  }
  .canvas {
    position: relative;
    width: 1200px;
    height: 900px;
  }

  /* Back of envelope: full blue */
  .envelope-back {
    position: absolute;
    left: 105px;
    top: 75px;
    width: 698px;
    height: 496px;
    background: var(--brand-blue);
    overflow: hidden;
  }
  .envelope-back .back-wave {
    position: absolute;
    inset: 0;
  }
  .envelope-back .wordmark-large {
    position: absolute;
    left: 108px;
    top: 168px;
    color: var(--paper);
    font-size: 82px;
    line-height: 1;
    letter-spacing: 1px;
    white-space: nowrap;
  }

  /* Front of envelope: white with blue band and wave */
  .envelope-front {
    position: absolute;
    left: 433px;
    top: 323px;
    width: 698px;
    height: 496px;
    background: var(--paper);
    overflow: hidden;
  }
  .envelope-front .header-band {
    position: absolute;
    left: 0;
    top: 40px;
    width: 100%;
    height: 72px;
    background: var(--brand-blue);
  }
  .envelope-front .wordmark-small {
    position: absolute;
    left: 72px;
    top: 21px;
    color: var(--paper);
    font-size: 26px;
    line-height: 1;
    white-space: nowrap;
  }
  .envelope-front .sender-details {
    position: absolute;
    left: 72px;
    top: 120px;
    color: var(--text-blue);
    font-size: 11.5px;
    line-height: 16px;
    letter-spacing: 0.6px;
  }
  .envelope-front .sender-details .web {
    display: block;
    margin-top: 3px;
    font-weight: 700;
    letter-spacing: 0.8px;
  }
  .envelope-front .footer-wave {
    position: absolute;
    inset: 0;
  }
</style>
</head>
<body>
  <main class="canvas">
    <section class="envelope-back" aria-label="Envelope back">
      <svg class="back-wave" width="698" height="496" viewBox="0 0 698 496" aria-hidden="true">
        <path d="M0,430 C140,448 260,430 380,405 C470,386 560,370 698,372 L698,398 C570,398 480,414 390,434 C270,460 140,476 0,462 Z"
              fill="var(--brand-blue-deep)"/>
      </svg>
      <div class="wordmark-large">Tallow Meadow</div>
    </section>

    <section class="envelope-front" aria-label="Envelope front">
      <div class="header-band">
        <div class="wordmark-small">Tallow Meadow</div>
      </div>
      <address class="sender-details" style="font-style: normal;">
        48 Linden Row<br>
        Harbourvale NSW 2150
        <span class="web">www.tallowmeadow.com</span>
      </address>
      <svg class="footer-wave" width="698" height="496" viewBox="0 0 698 496" aria-hidden="true">
        <path d="M0,320 C40,430 200,490 345,496 C450,480 560,446 640,452 C680,456 698,476 698,496 L0,496 Z"
              fill="var(--brand-blue)"/>
      </svg>
    </section>
  </main>
</body>
</html>
```